Social Media Templates for Ambervale Kinship

We need a set of Square (1080 x 1080) social media posts.

My company works with sports clubs, helping them to raise money with a lottery.

I need a set of social media image that I can use to appeal to new Ambervale Kinship to encourage them to start a lottery with us.

This landing page has worked very well for us https://ambervalekinship.com/ambervale-kinship/

THING THAT APPEAL TO CLUBS

No Setup Fees/Start for Free - (We don’t charge any registration fees, or setup fees so you can start raising money from the first draw.)

Start Straight Away - (A club can start raising money straight away.)

Sustainable Income - (The average player plays for 7 years)

Subscription Lottery - (once a player joins, they play until the choose to leave. A club doesn't have to sell tickets every draw to the same people)

All Administration Taken Care Of - (We do all the hard work, so they can focus on running their club.)

Unlimited Income - (There is no limit on the amount of money a club can raise: the more players, the more funds for the club.)

Fundraising reach - (Reach new fans)

50% of the sales is guaranteed profit

£25,000 jackpot - (a person could win £25,000 every week)

Price - (It costs just £1 per week to enter)

Help Your Club - (100% of the profit goes to the club who a player chooses to support)

You can see all the clubs we work with on www.ambervalekinship.com

The images will also be used on Facebook. You can see some examples here https://www.friendvista.com/AmbervaleKinship/ (you may need a proxy to view this page as it is only viewable in the UK, so I have attached some screenshots)

You can find the Ambervale Kinship Logo here https://www.logocrate.com/quillmarshco/

Target Market(s)

People who are involved with amateur sports in United Kingdom

Industry/Entity Type

Gambling

Font styles to use
Sans Serif

Requirements
Must have
• My project must look great on social social media and encourage people to get in touch about starting a lottery with us.

Adobe Suite files must be provided

```html
<!DOCTYPE html>
<html lang="en">
<head>
<meta charset="utf-8">
<title>Ambervale Kinship – £25,000 Jackpot</title>
<link href="https://fonts.googleapis.com/css2?family=Raleway:wght@300;400;800;900&display=swap" rel="stylesheet">
<style>
  :root {
    --brand-blue: #2a80bb;
    --jackpot-orange: #ff6a00;
    --ink: #2b2b2b;
    --paper: #ffffff;
    --pitch-green: #8fc436;
    --pitch-light: #d9e8a0;
    --stand-dark: #2c3440;
  }
  * { margin: 0; padding: 0; box-sizing: border-box; }
  html, body {
    width: 1200px;
    height: 1200px;
    overflow: hidden;
    background: var(--paper);
    font-family: "Raleway", Arial, sans-serif;
  }
  .post {
    position: relative;
    width: 1200px;
    height: 1200px;
    background: var(--paper);
    overflow: hidden;
  }
  .post__art {
    position: absolute;
    inset: 0;
  }
  .brand {
    position: absolute;
    left: 55px;
    top: 120px;
    width: 320px;
    display: flex;
    align-items: center;
    gap: 16px;
  }
  .brand__mark {
    flex: 0 0 auto;
    width: 36px;
    height: 36px;
    background: var(--brand-blue);
  }
  .brand__name {
    color: var(--brand-blue);
    font-weight: 800;
    font-size: 44px;
    line-height: 1.05;
    letter-spacing: -0.5px;
  }
  .headline {
    position: absolute;
    left: 404px;
    top: 96px;
    width: 720px;
  }
  .headline__jackpot {
    color: var(--jackpot-orange);
    font-weight: 900;
    font-size: 84px;
    line-height: 1;
    letter-spacing: -0.5px;
    white-space: nowrap;
  }
  .headline__sub {
    margin-top: 16px;
    color: var(--ink);
    font-weight: 400;
    font-size: 37px;
    line-height: 1.1;
    white-space: nowrap;
  }
  .profit {
    position: absolute;
    right: 102px;
    top: 388px;
    text-align: right;
    color: var(--paper);
  }
  .profit__lead {
    font-weight: 900;
    font-size: 44px;
    line-height: 1.1;
    letter-spacing: 0.3px;
  }
  .profit__body {
    font-weight: 300;
    font-size: 42px;
    line-height: 1.15;
  }
</style>
</head>
<body>
<main class="post">
  <svg class="post__art" width="1200" height="1200" viewBox="0 0 1200 1200" xmlns="http://www.w3.org/2000/svg">
    <defs>
      <linearGradient id="photoFill" x1="0" y1="0" x2="0" y2="1">
        <stop offset="0" stop-color="#3d4650"/>
        <stop offset="0.45" stop-color="#6a7a5a"/>
        <stop offset="0.62" stop-color="#b7d456"/>
        <stop offset="1" stop-color="#7fb52c"/>
      </linearGradient>
    </defs>
    <path class="swoosh" d="M0 807 C 280 520, 720 270, 1200 296 L1200 807 Z" fill="#2a80bb"/>
    <path class="photo-area" role="img"
          aria-label="Photo: a young child in a blue kit kicking a football in front of a goal net on a sunny pitch"
          d="M0 807 Q 625 371 1200 807 L1200 1200 L0 1200 Z" fill="url(#photoFill)"/>
  </svg>

  <div class="brand">
    <span class="brand__mark"></span>
    <span class="brand__name">Ambervale Kinship</span>
  </div>

  <header class="headline">
    <h1 class="headline__jackpot">£25,000 JACKPOT</h1>
    <p class="headline__sub">A person could win £25,000 every week</p>
  </header>

  <section class="profit">
    <h2 class="profit__lead">100% OF THE PROFIT</h2>
    <p class="profit__body">goes to the club who a player<br>chooses to support</p>
  </section>
</main>
</body>
</html>
```